Tavo's Spice Blend Dry Roasted and Freshly Ground Spices to create the Authentic and Aromatic Maur

I need a packaging design for a new company based in Kent called Tavo's Spice Blend. the size of the packaging will be for a 250gm bag.

I would like bright colours so that it can stand out from out the other products on a super market shelf

The packaging must have the list of ingredients on the back;

I.e. Ingredients;
Cumin
Coriander
Dried Red Chili
Cinnamon
Cloves
Cardamon
Black Peppercorn
Rice

Reason: Not enough designed to choose from. Tavo's Spice Blend, Dry Roasted and Freshly Ground Spices to create the Authentic and Aromatic flavour Please also add Turmeric to the ingredient list Thank you Bronna Castell

```html
<!DOCTYPE html>
<html lang="en">
<head>
<meta charset="utf-8">
<title>Tavo's Spice Blend – 250gm Pouch</title>
<link href="https://fonts.googleapis.com/css2?family=Tinos:wght@400;700&family=PT+Sans:wght@700&display=swap" rel="stylesheet">
<style>
  :root {
    --stage: #ffffff;
    --crimp: #e2b824;
    --maroon: #8e1a1c;
    --maroon-dark: #6e1012;
    --header-text: #fbeee0;
    --ink: #111111;
    --leaf: #4f9a2e;
    --front-bg: #f4f4f2;
    --back-yellow: #f1cc1c;
    --back-yellow-light: #fbe98a;
    --food-red: #a8321c;
  }
  * { box-sizing: border-box; margin: 0; padding: 0; }
  html, body { width: 1200px; height: 754px; overflow: hidden; background: var(--stage); }
  .canvas { position: relative; width: 1200px; height: 754px; }

  .pouch { position: absolute; top: 26px; width: 524px; height: 652px; overflow: hidden; }
  .pouch--front { left: 36px; background: var(--front-bg); }
  .pouch--back { left: 642px; background: radial-gradient(ellipse at 50% 35%, var(--back-yellow-light) 0%, var(--back-yellow) 60%, #e7b712 100%); }

  .crimp { position: absolute; left: 0; right: 0; height: 26px; background: repeating-linear-gradient(90deg, var(--crimp) 0 3px, #d3a917 3px 5px); z-index: 2; }
  .crimp--top { top: 0; }
  .crimp--bottom { bottom: 0; background: repeating-linear-gradient(90deg, #e8e6e0 0 3px, #d6d4cc 3px 5px); }
  .pouch--back .crimp--bottom { background: repeating-linear-gradient(90deg, #e9e6dc 0 3px, #d8d3c4 3px 5px); }

  .header-band { position: absolute; top: 26px; left: 0; width: 524px; height: 120px; }
  .product-name {
    position: absolute; top: 38px; left: 0; width: 524px; text-align: center;
    font-family: "PT Sans", Arial, sans-serif; font-weight: 700; font-size: 33px; line-height: 40px;
    color: var(--header-text);
  }

  .brand { font-family: "Tinos", "Times New Roman", serif; font-weight: 400; color: var(--ink); display: flex; align-items: center; gap: 10px; }
  .brand-dot { width: 14px; height: 14px; border-radius: 50%; background: var(--leaf); }
  .pouch--front .brand { position: absolute; top: 238px; left: 46px; font-size: 62px; line-height: 1; }
  .tagline { position: absolute; top: 316px; left: 42px; font-family: "Tinos", "Times New Roman", serif; font-size: 27px; color: var(--ink); }

  .photo { position: absolute; }
  .photo--spoons { top: 192px; left: 332px; width: 170px; height: 106px; border-radius: 8px;
    background: radial-gradient(ellipse at 40% 55%, #c98a3a 0%, #b05a2a 40%, rgba(244,244,242,0) 75%); }
  .photo--meatballs { left: 0; bottom: 26px; width: 524px; height: 270px;
    background: linear-gradient(180deg, rgba(244,244,242,0) 0%, #c9a67a 25%, var(--food-red) 55%, #e8d3a0 100%); }
  .net-weight { position: absolute; right: 18px; bottom: 48px; font-family: "Tinos", serif; font-weight: 700; font-size: 10px; color: var(--ink); }

  .pouch--back .brand { position: absolute; top: 62px; left: 0; width: 524px; justify-content: center; font-size: 50px; line-height: 1; }
  .ingredients { position: absolute; top: 126px; left: 0; width: 524px; text-align: center; font-family: "Tinos", "Times New Roman", serif; color: var(--ink); }
  .ingredients h2 { font-size: 19px; font-weight: 700; letter-spacing: 0.3px; }
  .ingredients p { font-size: 17px; line-height: 23px; margin-top: 3px; }
  .photo--dish { top: 236px; left: 152px; width: 224px; height: 104px; border-radius: 50%;
    background: radial-gradient(ellipse at center, var(--food-red) 0%, #c0652c 45%, #f3efe4 72%, #e2ddd0 100%); }
  .maker { position: absolute; top: 376px; left: 0; width: 524px; text-align: center; font-family: "Tinos", "Times New Roman", serif; font-size: 17px; line-height: 23px; color: var(--ink); z-index: 1; }
  .maker h3 { font-size: 17px; font-weight: 700; }
  .photo--spice-bowls { left: 0; bottom: 26px; width: 140px; height: 240px;
    background: linear-gradient(180deg, rgba(241,204,28,0) 0%, #b8321e 25%, #d89a2a 55%, #7a4a2a 100%); }
  .photo--mortar { right: 0; bottom: 26px; width: 134px; height: 180px;
    background: linear-gradient(180deg, rgba(241,204,28,0) 0%, #5a5450 40%, #7a4a2a 100%); }
  .photo--spice-floor { left: 0; bottom: 26px; width: 524px; height: 70px;
    background: linear-gradient(90deg, #9a4a22 0%, #c98a3a 30%, #e9d9a8 50%, #8a5a34 75%, #6a3a22 100%); }
  .side-note { position: absolute; top: 190px; right: 14px; writing-mode: vertical-rl; transform: rotate(180deg);
    font-family: "Tinos", serif; font-size: 14px; color: var(--ink); }
</style>
</head>
<body>
<main class="canvas">
  <section class="pouch pouch--front" aria-label="Front of pouch">
    <div class="crimp crimp--top"></div>
    <svg class="header-band" viewBox="0 0 524 120" aria-hidden="true">
      <path d="M0 0 H524 V24 L470 24 C460 100 420 118 262 118 C104 118 64 100 54 24 L0 24 Z" fill="var(--maroon)"/>
      <path d="M0 24 H54 C64 100 104 118 262 118 C420 118 460 100 470 24 H524" fill="none" stroke="var(--maroon-dark)" stroke-width="3"/>
    </svg>
    <h1 class="product-name">Tavo's<br>Spice Blend</h1>
    <div class="photo photo--spoons" role="img" aria-label="Wooden spoons holding ground spices"></div>
    <div class="brand"><span class="brand-dot"></span>Tavo's</div>
    <p class="tagline">The Real Taste of Pure Spices</p>
    <div class="photo photo--meatballs" role="img" aria-label="Meatballs in tomato sauce on spaghetti with parsley"></div>
    <span class="net-weight">250 gm</span>
    <div class="crimp crimp--bottom"></div>
  </section>

  <section class="pouch pouch--back" aria-label="Back of pouch">
    <div class="crimp crimp--top"></div>
    <div class="brand"><span class="brand-dot"></span>Tavo's</div>
    <div class="ingredients">
      <h2>INGREDIENTS</h2>
      <p>Cumin, Coriander, Dried Red Chili, Cinnamon, Cloves,<br>Cardamon, Black Peppercorn, Turmeric, Rice</p>
    </div>
    <div class="photo photo--dish" role="img" aria-label="Plate of spiced stir-fried chicken with peppers"></div>
    <div class="photo photo--spice-bowls" role="img" aria-label="Bowls of chilies, turmeric, peppercorns and whole spices"></div>
    <div class="photo photo--mortar" role="img" aria-label="Stone mortar with star anise and cinnamon"></div>
    <div class="photo photo--spice-floor" role="img" aria-label="Scattered whole spices"></div>
    <div class="maker">
      <h3>Manufactured By:</h3>
      <p>Unit 6, Orchard Way,<br>Maidstone, Kent ME14 2LT.<br>Tel: 01-4820 3157/ 3158<br>Fax: 02-4820 3160<br>Website: www.tavosspice.co.uk<br>Email: hello@tavosspice.co.uk</p>
    </div>
    <p class="side-note">Dry roasted, freshly ground</p>
    <div class="crimp crimp--bottom"></div>
  </section>
</main>
</body>
</html>
```